Meridane Haulage - Website

A clean, not cluttered informative website for our business. We specialize in the transportation of radioactive materials across North America. The site is mostly for information about our company and will not be used to attract business but will be used to attract employee's mainly drivers. Driver's are very hard to find in our area. One of the pages needs to be a job's posting page with an apply now button. Either an application can be filled out there or a resume can be uploaded which ever functionality works better. I would like a website that I can easily edit, ability to change text and photos.

Number of Pages Required

5+ page

Colors

Designer to choose colors to be used in the design.

Requirements
Must have
• Home - About - Services - Jobs - Contact pages
• A way prospective employee's can apply or upload their resume to be emailed to me
• Very clean apperance
Should not have
• I don't want it to be busy

```html
<!DOCTYPE html>
<html lang="en">
<head>
<meta charset="utf-8">
<title>Meridane Haulage – Website Design</title>
<link href="https://fonts.googleapis.com/css2?family=Montserrat:wght@300;400;500;600;700&display=swap" rel="stylesheet">
<style>
:root{
  --red:#e3161f;
  --ink:#111111;
  --dark:#1b1b1d;
  --grey-text:#6b6b6b;
  --body-text:#3a3a3a;
  --panel:#f5f5f5;
  --field-line:#e6e6e6;
  --tab-grey:#dedede;
  --vacancy-grey:#808080;
  --white:#ffffff;
}
*{box-sizing:border-box;margin:0;padding:0}
html,body{width:1040px;height:1200px;overflow:hidden;background:var(--white)}
body{font-family:'Montserrat',sans-serif;color:var(--body-text)}
.stage{position:absolute;left:0;top:0;width:1310px;height:1512px;transform:scale(0.7937);transform-origin:0 0}
.abs{position:absolute}
.page{position:absolute;background:var(--white);box-shadow:6px 6px 10px rgba(0,0,0,.35);overflow:hidden}
.page-home{left:44px;top:22px;width:599px;height:1244px}
.page-jobs{left:676px;top:20px;width:599px;height:1246px}

/* hero */
.hero{left:0;top:0;width:599px;background:linear-gradient(180deg,#2a2a2c 0%,#1a1a1b 60%,#121213 100%)}
.hero-sun{border-radius:50%;background:radial-gradient(circle at 40% 40%,#f01a22,#b50f16)}
.hero-cargo{background:linear-gradient(180deg,rgba(200,20,28,.0),rgba(200,20,28,.55))}
.brand{font-weight:700;font-size:17px;letter-spacing:1px;color:var(--red);display:flex;align-items:center;gap:6px}
.brand-dot{width:8px;height:8px;background:var(--red);border-radius:50%}
.nav{font-size:8.5px;color:var(--white)}
.nav span{position:absolute;white-space:nowrap}
.nav .active{color:var(--red)}
.hero-title{right:66px;text-align:right;color:var(--white);font-weight:700;font-size:21px;line-height:37px;white-space:nowrap}

/* about */
.about-card{left:50px;top:290px;width:499px;height:181px;background:var(--white)}
.about-text{left:30px;top:24px;width:205px}
.section-title{font-weight:600;color:var(--grey-text);font-size:15px;letter-spacing:.3px}
.small-copy{font-size:6.7px;line-height:8.2px;color:var(--body-text);margin-top:8px}
.btn{position:absolute;font-size:6.5px;display:flex;align-items:center;justify-content:center;white-space:nowrap}
.btn-dark{background:var(--ink);color:var(--white)}
.btn-red{background:var(--red);color:var(--white)}
.btn-grey{background:#3e3e3e;color:var(--white)}
.btn-outline-red{border:1px solid var(--red);color:var(--white)}
.btn-outline-white{border:1px solid var(--white);color:var(--white)}
.about-photo{left:249px;top:0;width:250px;height:181px;background:linear-gradient(135deg,#b7c6e6 0%,#eef1f8 45%,#9fb1da 100%)}

/* services */
.services-band{left:0;top:366px;width:599px;height:307px;background:var(--panel)}
.service-card{width:114px;height:87px;background:#efefef;text-align:center}
.service-icon{position:absolute;left:31px;top:14px;width:52px;height:52px;border:2px solid var(--ink);border-radius:4px}
.service-label{position:absolute;left:0;right:0;top:78px;font-size:7px;font-weight:500;color:var(--ink)}
.service-list{font-size:7px;line-height:12.5px;color:var(--body-text);white-space:nowrap}

/* driver band */
.driver-band{left:0;top:830px;width:599px;height:199px;background:#000}
.driver-circle{border-radius:50%;background:var(--red)}
.driver-ring{border:4px solid #5a3a14;border-radius:50%}
.driver-photo{background:linear-gradient(160deg,#41577c 0%,#7d6a58 45%,#2f4b76 100%)}
.kicker{font-weight:700;font-size:14px;color:var(--white);white-space:nowrap}
.driver-heading{font-weight:300;font-size:26px;color:var(--white);white-space:nowrap}

/* contact */
.map{left:0;top:1029px;width:599px;height:195px;background:linear-gradient(120deg,#c9e3bf 0%,#ececea 20%,#f1f1ef 70%,#e4e4e2 100%)}
.map-pin{width:10px;height:10px;border-radius:50% 50% 50% 0;background:var(--red);transform:rotate(-45deg)}
.contact-card{left:263px;top:1063px;width:287px;height:143px;background:var(--white);box-shadow:2px 3px 6px rgba(0,0,0,.3)}
.field{position:absolute;border:1px solid var(--field-line);font-size:5px;color:#a0a0a0;padding:5px 6px}
.footer{left:0;bottom:0;width:599px;height:20px;background:#000;color:var(--red);font-size:5.5px;display:flex;align-items:center;justify-content:center}
.page-label{font-size:9px;color:var(--ink);border-bottom:3px solid var(--red);padding:0 8px;white-space:nowrap}

/* jobs */
.jobs-hero{left:0;top:0;width:599px;height:220px;background:linear-gradient(180deg,#2c2c2e,#151516)}
.jobs-title{left:49px;top:121px;color:var(--white);font-weight:700;font-size:17px}
.jobs-grey{left:0;top:220px;width:599px;height:308px;background:var(--panel)}
.intro-card{left:49px;top:201px;width:499px;height:132px;background:var(--white)}
.form-card{left:48px;top:352px;width:500px;height:231px;background:var(--white);border:1px solid #d6d6d6}
.tab{position:absolute;top:0;height:40px;display:flex;align-items:center;justify-content:center;font-size:13px;letter-spacing:.3px}
.tab-active{left:0;width:249px;color:var(--ink);background:var(--white)}
.tab-idle{left:249px;width:250px;background:var(--tab-grey);color:#8a8a8a;border-bottom:1px solid #cfcfcf}
.vac-title{left:0;width:599px;top:618px;text-align:center;font-weight:700;color:var(--grey-text);font-size:15.5px}
.job-name{left:49px;top:656px;font-size:11px;color:var(--ink)}
.job-body{left:47px;top:677px;width:500px;font-size:7.9px;line-height:11px;color:var(--body-text)}
.job-body p{margin-bottom:11px}
.other-title{left:47px;top:1016px;font-weight:700;color:var(--grey-text);font-size:15.5px}
.vacancy-tile{top:1048px;width:159px;height:127px;background:var(--vacancy-grey)}

/* offer panel */
.offer{left:57px;top:1330px;width:1218px;height:182px;border:1px solid #c44a57;border-bottom:none}
.offer-divider{left:547px;top:20px;width:1px;height:140px;background:#555}
.offer-text{font-size:13.5px;line-height:18px;color:var(--ink);white-space:nowrap}
.offer-paid{color:var(--red)}
.offer-paid small{font-style:italic;font-size:9px;display:block;line-height:16px}
</style>
</head>
<body>
<div class="stage">

  <!-- HOME PAGE -->
  <section class="page page-home">
    <div class="abs hero" style="height:366px">
      <div class="abs hero-sun" role="img" aria-label="Red sun behind winter trees" style="left:405px;top:96px;width:200px;height:200px"></div>
      <div class="abs hero-cargo" role="img" aria-label="Photo of a truck hauling tanks of radioactive cargo" style="left:100px;top:170px;width:499px;height:196px"></div>
    </div>
    <div class="abs brand" style="left:39px;top:26px"><span class="brand-dot"></span>Meridane Haulage</div>
    <nav class="nav abs" style="left:0;top:29px;width:599px">
      <span class="active" style="left:276px">Home</span>
      <span style="left:332px">About</span>
      <span style="left:387px">Services</span>
      <span style="left:450px">Jobs</span>
      <span style="left:498px">Contact</span>
    </nav>
    <h1 class="abs hero-title" style="top:119px">TRANSPORTATION<br>OF RADIOACTIVE MATERIALS<br>ACROSS NORTH AMERICA</h1>

    <div class="abs services-band"></div>

    <div class="abs about-card">
      <div class="abs about-text">
        <h2 class="section-title">ABOUT US</h2>
        <p class="small-copy">Lorem ipsum dolor sit amet, consectetuer adipiscing elit, sed diam nonummy nibh euismod tincidunt ut laoreet dolore Lorem ipsum dolor sit amet, consectetuer adipiscing elit, sed diam nonummy nibh euismod tincidunt ut laoreet dolore Lorem ipsum dolor sit amet, consectetuer adipiscing elit, sed diam nonummy nibh euismod tincidunt ut</p>
      </div>
      <div class="btn btn-dark" style="left:30px;top:133px;width:72px;height:20px">Learn More</div>
      <div class="abs about-photo" role="img" aria-label="Photo of a white truck on the road"></div>
    </div>

    <h2 class="abs section-title" style="left:0;width:599px;top:522px;text-align:center">SERVICES</h2>
    <div class="abs service-card" style="left:50px;top:572px"><div class="service-icon" role="img" aria-label="Hazard container icon"></div><div class="service-label">SERVICE 1</div></div>
    <div class="abs service-card" style="left:177px;top:572px"><div class="service-icon" role="img" aria-label="Radiation facility icon"></div><div class="service-label">SERVICE 2</div></div>
    <div class="abs service-card" style="left:305px;top:572px"><div class="service-icon" role="img" aria-label="Storage site icon"></div><div class="service-label">SERVICE 3</div></div>
    <div class="abs service-card" style="left:433px;top:572px"><div class="service-icon" role="img" aria-label="Cargo transport icon"></div><div class="service-label">SERVICE 4</div></div>

    <div class="abs service-list" style="left:67px;top:707px">· Service Lorem ipsum dolum<br>· Service Lorem ipsum dolum<br>· Service Lorem ipsum dolum<br>· Service Lorem ipsum dolum</div>
    <div class="abs service-list" style="left:223px;top:707px">· Service Lorem ipsum dolum<br>· Service Lorem ipsum dolum<br>· Service Lorem ipsum dolum<br>· Service Lorem ipsum dolum</div>
    <div class="abs service-list" style="left:385px;top:707px">· Service Lorem ipsum dolum<br>· Service Lorem ipsum dolum<br>· Service Lorem ipsum dolum<br>· Service Lorem ipsum dolum</div>

    <div class="abs driver-band"></div>
    <div class="abs driver-circle" style="left:-40px;top:815px;width:140px;height:118px;border-radius:50%"></div>
    <div class="abs driver-ring" style="left:345px;top:856px;width:230px;height:230px"></div>
    <div class="abs driver-photo" role="img" aria-label="Photo of a smiling truck driver in a cap and denim jacket" style="left:400px;top:806px;width:199px;height:223px;border-radius:80px 80px 0 0"></div>
    <div class="abs kicker" style="left:50px;top:881px">ARE YOU A DRIVER?</div>
    <div class="abs driver-heading" style="left:89px;top:902px">Work With Us</div>
    <div class="btn btn-outline-red" style="left:92px;top:962px;width:115px;height:21px">Apply Now Your Resume</div>
    <div class="btn btn-outline-white" style="left:217px;top:961px;width:102px;height:21px">Browse Job Vacancies</div>

    <div class="abs map" role="img" aria-label="Street map showing the company location"></div>
    <div class="abs map-pin" style="left:138px;top:1134px"></div>
    <div class="abs contact-card">
      <div class="field" style="left:24px;top:16px;width:106px;height:15px">Full Name</div>
      <div class="field" style="left:135px;top:16px;width:111px;height:15px">Email</div>
      <div class="field" style="left:24px;top:37px;width:222px;height:15px">Subject</div>
      <div class="field" style="left:24px;top:58px;width:222px;height:40px">Your Message</div>
      <div class="btn btn-dark" style="left:24px;top:106px;width:58px;height:20px">Submit</div>
    </div>
    <div class="abs footer">2019 - Meridane Haulage</div>
  </section>
  <div class="abs page-label" style="left:312px;top:1283px">HOMEPAGE</div>

  <!-- JOBS PAGE -->
  <section class="page page-jobs">
    <div class="abs jobs-hero" role="img" aria-label="Photo of parked trucks in dark tones"></div>
    <div class="abs brand" style="left:39px;top:28px"><span class="brand-dot"></span>Meridane Haulage</div>
    <nav class="nav abs" style="left:0;top:31px;width:599px">
      <span style="left:276px">Home</span>
      <span style="left:332px">About</span>
      <span style="left:387px">Services</span>
      <span class="active" style="left:450px">Jobs</span>
      <span style="left:498px">Contact</span>
    </nav>
    <h1 class="abs jobs-title">WORK WITH US</h1>
    <div class="abs jobs-grey"></div>
    <div class="abs intro-card">
      <p class="abs small-copy" style="left:27px;top:22px;width:445px;margin:0">Lorem ipsum dolor sit amet, consectetuer adipiscing elit, sed diam nonummy nibh euismod tincidunt ut laoreet dolore Lorem ipsum dolor sit amet, consectetuer adipiscing elit, sed diam nonummy nibh euismod tincidunt ut laoreet dolore Lorem ipsum dolor sit amet, consectetuer adipiscing elit, sed diam nonummy nibh euismod tincidunt ut laoreet dolore</p>
      <div class="btn btn-red" style="left:28px;top:83px;width:113px;height:19px">Apply Now Your Resume</div>
      <div class="btn btn-grey" style="left:154px;top:83px;width:101px;height:19px">Browse Job Vacancies</div>
    </div>
    <div class="abs form-card">
      <div class="tab tab-active">FILL THE APPLICATION</div>
      <div class="tab tab-idle">UPLOAD YOUR RESUME</div>
      <div class="field" style="left:28px;top:64px;width:142px;height:24px">Name</div>
      <div class="field" style="left:176px;top:64px;width:142px;height:24px">Surname</div>
      <div class="field" style="left:324px;top:64px;width:142px;height:24px">Phone</div>
      <div class="field" style="left:28px;top:94px;width:142px;height:24px">Email</div>
      <div class="field" style="left:176px;top:94px;width:142px;height:24px">Experience<svg class="abs" style="right:8px;top:9px" width="8" height="5" viewBox="0 0 8 5"><path d="M0 0 L4 4 L8 0" fill="none" stroke="#999" stroke-width="1"/></svg></div>
      <div class="field" style="left:324px;top:94px;width:142px;height:24px">Certificate<svg class="abs" style="right:8px;top:9px" width="8" height="5" viewBox="0 0 8 5"><path d="M0 0 L4 4 L8 0" fill="none" stroke="#999" stroke-width="1"/></svg></div>
      <div class="field" style="left:28px;top:124px;width:290px;height:24px">Last company</div>
      <div class="field" style="left:324px;top:124px;width:142px;height:24px">Time Worked</div>
      <div class="field" style="left:28px;top:154px;width:142px;height:24px">Desired Salary</div>
      <div class="field" style="left:176px;top:154px;width:290px;height:24px"></div>
      <div class="btn btn-dark" style="left:28px;top:188px;width:58px;height:20px">Submit</div>
    </div>

    <h2 class="abs vac-title">JOB VACANCIES</h2>
    <h3 class="abs job-name" style="font-weight:400">Security Van/7.5T Drivers</h3>
    <div class="abs job-body">
      <p>We're looking for adaptable and flexible individuals to join our Northern Depot. You will be securely loading, transporting &amp; delivering specialised freight namely Dangerous Goods (UN Hazardous Classes 1-9 including explosives &amp; radioactive material), sensitive &amp; prohibited items to client's sites in accordance with ADR legislation and the Company's Security Plan adhering to strict daily schedules.</p>
      <p>Daily tasks will include:</p>
      <p>Accommodation moves (furniture and IT equipment)<br>Delivery and installation/build of furniture<br>Asset recovery and disposal<br>Conference room set up including the building of click kits<br>The collection, delivery and distribution of items internally and externally such as post, calibration equipment, bioassay and air samples<br>Escorting vehicles around site, driving a CTS escort vehicle<br>Other ad hoc doc duties as they arise<br>Safe operation of manual handling equipment: forklift, electric reach, cabinet lifters, stair walkers hand operated pallet trucks and vehicles with tail-lifts</p>
      <p>Required:</p>
      <p>7.5T licence (max 3 points, no DD/DR/IT points or disqualifications) held for at least 12 months with at least 12 months' commercial driving experience<br>Good knowledge of WTD and Drivers Hours Legislation<br>Professional defense driving skills with ability to remain focused when driving for long periods<br>Good geographical knowledge with experience of driving throughout UK and into Europe<br>Adaptability/flexibility on hours as scheduling can be subject to last minute changes<br>Security clearance is a requirement of the role so applicants must hold 5 years' UK residency and a 5 year verifiable employment history<br>Desirable:</p>
    </div>
    <h2 class="abs other-title">OTHER VACANCIES</h2>
    <div class="abs vacancy-tile" style="left:47px"></div>
    <div class="abs vacancy-tile" style="left:218px"></div>
    <div class="abs vacancy-tile" style="left:390px"></div>
    <div class="abs footer">2019 - Meridane Haulage</div>
  </section>
  <div class="abs page-label" style="left:950px;top:1281px">JOBS PAGE</div>

  <!-- OFFER PANEL -->
  <section class="abs offer">
    <div class="abs offer-text" style="left:26px;top:14px">Hello,<br>I created a web design for you. Looking forward to your feedback.<br><br>I can create the fully functional LIVE DEMO for you if you want.<br>Just let me know.<br><br>Please note: As you did not provide any content for the website, I used the<br>dummy content as a sample. Any revisions are available</div>
    <div class="abs offer-divider"></div>
    <div class="abs offer-text" style="left:575px;top:27px">WHAT YOU"LL GET WITH THIS OFFER:<br><br>1. Fully functional responsive website<br>2. Files upload to your (or mine) hosting<br>3. Installation and configuration<br>4. Additional components and plugins<br>5. Additional graphic design, required for this website</div>
    <div class="abs offer-text" style="left:940px;top:52px">6. Professional support at anytime</div>
    <div class="abs offer-text offer-paid" style="left:940px;top:84px"><small>Paid service:</small>7. On page SEO<br>8. Administration &amp; Maintenance<br>9. Additional language installation</div>
  </section>

</div>
</body>
</html>
```